letterhead design

can you create a letterhead using the logo you created and the following:

318 W Dunthorpe Elgin IL 60187
(p) 847-512-3971
(f) 847-438-1065
www.thekestrinlawgroup.example

Industry/Entity Type

Law

Requirements
Must have
• Use logo attached: must have address 318 W Dunthorpe Elgin IL 60187 phone 847-512-3971 fax 847-438-1065
Should not have
• Nothing other thank logo and address/phone/website

```html
<!DOCTYPE html>
<html lang="en">
<head>
<meta charset="utf-8">
<title>Kestrin Law Group Letterhead</title>
<link href="https://fonts.googleapis.com/css2?family=Poppins:wght@300;400;600&display=swap" rel="stylesheet">
<style>
  :root {
    --paper: #ffffff;
    --gold: #e2b35a;
    --gold-faint: #faf5ea;
    --maroon: #43192a;
    --ink: #3a1a26;
  }
  html, body {
    margin: 0;
    padding: 0;
    width: 960px;
    height: 1200px;
    overflow: hidden;
    background: var(--paper);
  }
  .letterhead {
    position: relative;
    width: 960px;
    height: 1200px;
    background: var(--paper);
    font-family: "Poppins", sans-serif;
    overflow: hidden;
  }
  .brand {
    position: absolute;
    left: 70px;
    top: 62px;
    display: flex;
    align-items: center;
    gap: 12px;
  }
  .brand-mark {
    width: 84px;
    height: 84px;
    border: 2px solid var(--gold);
    border-radius: 50%;
    box-sizing: border-box;
  }
  .brand-name {
    font-family: "Poppins", sans-serif;
    font-weight: 300;
    font-size: 25px;
    letter-spacing: 0.5px;
    color: var(--gold);
    text-transform: uppercase;
    line-height: 1.25;
  }
  .contact {
    position: absolute;
    left: 610px;
    top: 46px;
    margin: 0;
    padding: 0;
    list-style: none;
    font-size: 15.5px;
    font-weight: 400;
    color: var(--ink);
    letter-spacing: 0.4px;
  }
  .contact li {
    display: flex;
    align-items: center;
    gap: 8px;
    height: 30px;
  }
  .contact svg { width: 13px; height: 13px; fill: var(--maroon); }
  .contact strong { font-weight: 600; }
  .backdrop-ring {
    position: absolute;
    left: 234px;
    top: 370px;
    width: 512px;
    height: 512px;
    border: 11px solid var(--gold-faint);
    border-radius: 50%;
    box-sizing: border-box;
  }
  .footer-rule {
    position: absolute;
    left: 0;
    top: 1169px;
    width: 612px;
    height: 5px;
    background: var(--gold);
  }
  .footer-band {
    position: absolute;
    left: 0;
    top: 1181px;
    width: 601px;
    height: 19px;
    background: var(--maroon);
  }
  .footer-block {
    position: absolute;
    left: 611px;
    top: 1169px;
    width: 349px;
    height: 31px;
    background: var(--gold);
  }
</style>
</head>
<body>
  <main class="letterhead">
    <header>
      <div class="brand">
        <div class="brand-mark" aria-hidden="true"></div>
        <div class="brand-name">Kestrin Law Group</div>
      </div>
      <ul class="contact">
        <li>318 W Dunthorpe Elgin IL 60187</li>
        <li>
          <svg viewBox="0 0 16 16" aria-label="Phone"><path d="M3 2h3l1.5 3.5-2 1.2a8 8 0 0 0 3.8 3.8l1.2-2L14 10v3a1 1 0 0 1-1 1A11 11 0 0 1 2 3a1 1 0 0 1 1-1z"/></svg>
          847-512-3971
        </li>
        <li>
          <svg viewBox="0 0 16 16" aria-label="Fax"><path d="M4 1h8v4H4zM1 6h14v7h-3v2H4v-2H1zM5 10v4h6v-4z"/></svg>
          847-438-1065
        </li>
        <li>www.<strong>thekestrinlawgroup</strong>.example</li>
      </ul>
    </header>
    <div class="backdrop-ring" aria-hidden="true"></div>
    <footer>
      <div class="footer-rule"></div>
      <div class="footer-band"></div>
      <div class="footer-block"></div>
    </footer>
  </main>
</body>
</html>
```